Online Digital Solutions Agency needs a New Business Card

We are a Online/Digital solution agency. We provide WordPress Solutions, Online & Digital Marketing Solutions including SEO, Social Media Marketing and Managed Hosting including VPS and Cloud Hosting solutions. We also design and build bespoke web sites and web applications for various clients. We are very good at site migrations, 3rd party API integrations and mobile app development.

We are rebranding our agency and have already designed a new logo. We have selected 5-6 colours as our base colour and are currently building our new website based around these colour scheme.

Our logo indicates that we are a cloud solution providers, and (i.e. the Clouds), and developers (i.e. HTML Tags, and CSS formats). We use the 5-6 base colours and use various shades of these colours as required.

Our old website is located at: www.brambleforgelabs.com

And our new website is going to be at (we are working on it at the moment ...):
https://creative.brambleforgelabs.co.uk/

Our slogan is "Digital Transformation Specialist"

What we mean by that is; we can take any existing business and get them up and transform them in to the digital world, starting with Hosting, Web Design, Development & Online Marketing aspects.

The powerpoint is a document that we use to present our projects to clients at the moment, and the cloud is on the background as we clarified earlier. (Just to get the idea)

What we are looking for is a Great WoW factor design to start with, ideally with the Logo and Logo colour scheme if possible but not required as long as the designers can do better, and basically give life to our logo and company via the Business card design.

Ideally with some icons perhaps to indicate the address, location, mobile, email, and website would be good but again optional as long as there is a good design.

The cloud can be used as a background if required in a light shade or as a watermark share perhaps.

The logos' and the Illustrator files are shared with you so you can use them as required.

Ideally the business card should have a Name, title, Mobile, Email , Website, Address and perhaps some social media links.

Target Market(s)

New Startups, SME's, Contract and Outsource Clients

Contact Information for Business Card

Company Name:
==============
BrambleForge Labs (UK) Ltd.

Tag Line:
========
“Digital Transformation Specialists”

Adress:
=======

Suite KR73054
14-16 Ashgrove Lane
London
E9 4PD.

Name:
=====
Idris Malek

Title: (Optional)
=============
FQTA, PgD (RNOM)

Role:
=====
Digital Solutions Architect

Email:
=====
idris@brambleforgelabs.uk

WebSite:
=======
http://www.brambleforgelabs.uk

OR

www.brambleforgelabs.uk

Mobile:
======
0044 (0)75 218 30479

OR

+44 (0)75 218 30479

LinkedIN: (Optional)
========
https://uk.linkedin.com/in/idrismalek

Skype: (Optional)
======
idris.malek

Twitter (Optional) : idrismalek

Font styles to use
Serif
Sans Serif

Requirements
Must have
• The Logo
• Business Name
• Person Name
• Title
• Mobile
• Email
• Website
• Address
• I have provided the colour scheme on my files.
Nice to have
• Twiter
• Linked in
• Facebook

```html
<!DOCTYPE html>
<html lang="en">
<head>
<meta charset="utf-8">
<title>BrambleForge Labs – Business Card</title>
<link rel="stylesheet" href="https://fonts.googleapis.com/css2?family=Arimo:wght@400;700&display=swap">
<style>
  :root {
    --brand-blue: #0f5aa8;
    --brand-navy: #0b4a90;
    --brand-sky: #2aa6de;
    --card-face: #f4f5f6;
    --ink: #1d2a3a;
    --stage: #d9dce0;
    --white: #ffffff;
  }
  html, body {
    margin: 0;
    width: 1200px;
    height: 997px;
    overflow: hidden;
    background: var(--stage);
    font-family: "Arimo", Arial, sans-serif;
  }
  .canvas {
    position: relative;
    width: 1200px;
    height: 997px;
  }
  .card {
    position: absolute;
    left: 280px;
    width: 640px;
    height: 366px;
    border-radius: 4px;
    overflow: hidden;
    box-shadow: 0 14px 34px rgba(0,0,0,.25);
  }
  /* Front */
  .card--front {
    top: 90px;
    background: radial-gradient(ellipse at 50% 45%, #2b82d4 0%, #1565b8 55%, #0d4f9e 100%);
    color: var(--white);
    display: flex;
    flex-direction: column;
    align-items: center;
    justify-content: center;
  }
  .front-brand {
    display: flex;
    align-items: center;
    gap: 14px;
    font-weight: 700;
    font-size: 46px;
    letter-spacing: -0.5px;
  }
  .brand-dot {
    width: 22px;
    height: 22px;
    border-radius: 50%;
    background: currentColor;
  }
  .front-tagline {
    margin-top: 26px;
    font-size: 15px;
    letter-spacing: 2.4px;
    text-transform: uppercase;
    color: #d6e6f6;
  }
  /* Back */
  .card--back {
    top: 540px;
    background: var(--card-face);
    color: var(--ink);
  }
  .back-brand {
    position: absolute;
    top: 62px;
    left: 240px;
    display: flex;
    align-items: center;
    gap: 12px;
    font-weight: 700;
    font-size: 38px;
    color: var(--brand-blue);
    letter-spacing: -0.5px;
  }
  .back-brand .brand-dot { width: 18px; height: 18px; background: var(--brand-sky); }
  .brand-rule {
    position: absolute;
    top: 128px;
    left: 250px;
    width: 360px;
    height: 1px;
    background: #2d2d2d;
  }
  .person {
    position: absolute;
    top: 160px;
    left: 34px;
  }
  .person__name {
    display: flex;
    align-items: center;
    gap: 6px;
    font-weight: 700;
    font-size: 15px;
    color: var(--brand-blue);
    text-transform: uppercase;
  }
  .person__name::after {
    content: "";
    width: 62px;
    height: 1px;
    background: #2d2d2d;
  }
  .person__role { font-size: 12.5px; margin-top: 2px; }
  .contact-list {
    position: absolute;
    top: 222px;
    left: 34px;
    margin: 0;
    padding: 0;
    list-style: none;
    font-size: 13.5px;
  }
  .contact-list li {
    display: flex;
    align-items: center;
    gap: 12px;
    height: 24px;
  }
  .contact-icon { width: 15px; height: 15px; flex: none; }
  .address {
    position: absolute;
    top: 198px;
    right: 40px;
    text-align: right;
    font-size: 12.5px;
    line-height: 1.35;
    color: var(--brand-blue);
  }
  .bands { position: absolute; left: 0; bottom: 0; }
  .website {
    position: absolute;
    right: 40px;
    bottom: 40px;
    font-weight: 700;
    font-size: 14px;
    letter-spacing: .6px;
    color: var(--white);
  }
</style>
</head>
<body>
<main class="canvas">

  <section class="card card--front" aria-label="Card front">
    <div class="front-brand"><span class="brand-dot"></span>BrambleForge Labs</div>
    <div class="front-tagline">Digital Transformation Specialists</div>
  </section>

  <section class="card card--back" aria-label="Card back">
    <div class="back-brand"><span class="brand-dot"></span>BrambleForge Labs</div>
    <div class="brand-rule"></div>

    <div class="person">
      <div class="person__name">Idris Malek</div>
      <div class="person__role">Digital Solutions Architect</div>
    </div>

    <ul class="contact-list">
      <li>
        <svg class="contact-icon" viewBox="0 0 16 16"><circle cx="8" cy="8" r="8" fill="var(--brand-navy)"/><path d="M4.5 9.5c0-2 1.6-3.3 3.5-3.3s3.5 1.3 3.5 3.3H10l-.6-1.4H6.6L6 9.5z" fill="#fff"/></svg>
        0044 (0)75 218 30479
      </li>
      <li>
        <svg class="contact-icon" viewBox="0 0 16 16"><circle cx="8" cy="8" r="8" fill="var(--brand-navy)"/><rect x="4" y="5.2" width="8" height="5.6" fill="none" stroke="#fff" stroke-width="1"/><path d="M4 5.4l4 3 4-3" fill="none" stroke="#fff" stroke-width="1"/></svg>
        idris@brambleforgelabs.uk
      </li>
      <li>
        <svg class="contact-icon" viewBox="0 0 16 16"><circle cx="8" cy="8" r="8" fill="var(--brand-navy)"/><circle cx="8" cy="8" r="3.4" fill="#fff"/></svg>
        idrismalek
      </li>
    </ul>

    <div class="address">14-16, Ashgrove Lane London<br>E9 4PD, United Kingdom</div>

    <svg class="bands" width="640" height="366" viewBox="0 0 640 366">
      <path d="M0 324 H300 C322 324 326 312 344 312 H360 C342 312 336 336 312 336 H0 Z" fill="var(--brand-sky)"/>
      <path d="M330 352 C352 352 352 296 384 296 H640 V366 H0 V352 Z" fill="var(--brand-navy)"/>
      <rect x="0" y="344" width="640" height="2" fill="var(--card-face)"/>
    </svg>
    <div class="website">www.brambleforgelabs.uk</div>
  </section>

</main>
</body>
</html>
```